Modern CNC Machining Facility in Need of Web Site Improvement

Brixton Fabrication and Tooling, LLC is in need of a web site update. We need to highlight both product sales and our manufacturing services offered. We have recently started offering online product sales and need a better ecommerce platform for our customers. We would like the design winner to be able to freelance the project to a fully functioning webpage.
www.brixtonfabrication.example
What we like about our current web site:
Black and red highlight colors
Gear and caliper logo
RNVR Veteran owned business
What we don't like about our current web site:
Unorganized
Doesn't stand out
Looks like it was made in 1995
Online Product sales are awkward

```html
<!DOCTYPE html>
<html lang="en">
<head>
<meta charset="utf-8">
<title>Brixton Fabrication and Tooling, LLC</title>
<link rel="stylesheet" href="https://fonts.googleapis.com/css2?family=Arimo:wght@400;700&family=Alegreya+SC:wght@500&family=Tinos&display=swap">
<style>
:root{
  --red:#b3161c;
  --red-dark:#8e0f13;
  --ink:#222;
  --text:#3a3a3a;
  --muted:#666;
  --nav:#1d1d1d;
  --line:#d9d9d9;
  --panel:#e9e9e9;
  --rust:#8a5a3c;
}
*{box-sizing:border-box;margin:0;padding:0}
html,body{width:881px;height:1200px;overflow:hidden;background:#fff}
body{position:relative;font-family:"Arimo",Arial,sans-serif;color:var(--text);font-size:10px;background:linear-gradient(#f0f0f0,#fff 90px)}
.abs{position:absolute}
a{color:inherit;text-decoration:underline}
/* header */
.brand-mark{left:98px;top:18px;width:86px;height:86px;border-radius:50%;background:var(--red);border:8px solid #2b2b2b}
.brand-name{left:205px;top:40px;width:300px;white-space:nowrap;font-family:"Alegreya SC",serif;font-weight:500;font-size:16px;color:var(--red);letter-spacing:0}
.brand-tag{left:205px;top:67px;font-family:"Tinos",serif;font-size:10.5px;color:#555}
.phone{right:93px;top:18px;font-size:13px;color:var(--red);display:flex;align-items:center;gap:5px}
.search{left:536px;top:54px;width:146px;height:24px;background:#e6e6e6;border-radius:3px;padding:7px 10px;font-size:9.5px;color:#555}
.search svg{position:absolute;right:5px;top:4px}
.cart{left:697px;top:56px;display:flex;align-items:center;gap:8px;font-size:11.5px;color:#333}
.nav{left:93px;top:116px;width:694px;height:28px;background:linear-gradient(#4a4a4a,var(--nav));border-radius:3px 3px 0 0;display:flex;justify-content:space-around;align-items:center;color:#fff;font-size:10px}
/* hero */
.hero{left:93px;top:157px;width:694px;height:257px;border:1px solid var(--line)}
.hero-photo{left:0;top:0;width:455px;height:255px;background:radial-gradient(ellipse at 50% 50%,#a0714f 0,#8a5a3c 25%,#f4f4f4 55%,#e8e8e8 100%)}
.hero-panel{left:455px;top:0;width:238px;height:255px;background:repeating-linear-gradient(135deg,#d4d4d4 0 1px,#c9c9c9 1px 3px);padding:44px 28px 0}
.hero-panel h2{font-weight:400;font-size:17px;color:var(--red);margin-bottom:12px}
.hero-panel p{font-size:9.3px;line-height:11.5px;color:#444;letter-spacing:.3px}
.hero-price{font-size:12.5px;color:var(--red);margin:13px 0 15px}
.buy{display:inline-block;width:87px;height:27px;background:linear-gradient(#d9232a,var(--red-dark));border-radius:3px;color:#fff;font-size:12.5px;text-align:center;line-height:27px}
.dots{right:25px;bottom:13px;display:flex;gap:4px}
.dots i{width:11px;height:11px;border-radius:50%;background:#fff;display:block}
.dots i.on{background:var(--red)}
/* welcome */
.welcome{left:93px;top:434px;width:432px;border-bottom:1px solid var(--line);padding-bottom:12px;font-size:15px;color:var(--ink)}
.welcome b{color:var(--red)}
.intro{left:93px;top:489px;width:432px;font-size:9.8px;line-height:11.6px;color:#333}
.intro-photo{float:left;width:146px;height:112px;border:1px solid var(--line);padding:4px;margin:0 16px 4px 0;background:#fff}
.intro-photo div{width:100%;height:100%;background:linear-gradient(135deg,#c21e24,#8f8f8f 55%,#3a3a3a)}
.intro h3{font-weight:400;font-size:12.5px;color:var(--red);margin:0 0 11px}
.intro p{margin-bottom:11px}
.veteran{left:93px;top:642px;display:flex;align-items:center;gap:6px}
.veteran-badge{width:42px;height:42px;border-radius:50%;background:#c9c9c9}
.veteran h4{font-weight:400;font-size:12.5px;color:var(--red);margin-bottom:10px}
.veteran span{font-family:"Tinos",serif;font-size:11px;color:#333;font-style:italic}
/* products */
.featured{left:93px;top:719px;width:432px;height:334px;background:#e6e6e6;border-radius:3px;box-shadow:0 1px 2px #bbb}
.featured-head{height:30px;background:linear-gradient(#555,#1f1f1f);border-radius:3px 3px 0 0;color:#fff;display:flex;justify-content:space-between;align-items:center;padding:0 12px}
.featured-head h3{font-weight:400;font-size:14px}
.featured-head a{font-size:9.5px}
.grid{display:grid;grid-template-columns:repeat(3,133px);column-gap:10px;row-gap:14px;padding:12px 6px 0}
.card-img{height:86px;background:#fff;padding:5px}
.card-img div{height:100%}
.wings{background:linear-gradient(#e8e8e8,#cfcfcf)}
.gears{background:radial-gradient(circle,#9a6a48,#d9d9d9 75%)}
.sun{background:radial-gradient(circle,#cfcfcf,#555 60%,#3c3c3c)}
.card-info{padding:9px 0 0;font-size:10px;color:var(--red);line-height:11.5px}
.card-links{display:flex;gap:14px;color:#222;font-size:8.5px;margin-top:2px;text-decoration:underline}
/* sidebar */
.side{left:574px;top:434px;width:213px}
.side-h{font-size:14px;color:var(--ink);display:flex;align-items:center;gap:8px;margin-bottom:16px}
.side-h b{color:var(--red);font-weight:700}
.side-h::after{content:"";flex:1;height:1px;background:var(--line)}
.industry{display:flex;gap:12px;height:66px}
.thumb{width:67px;height:54px;border:1px solid var(--line);padding:3px;flex:none}
.thumb div{height:100%}
.industry h5{font-weight:400;font-size:10px;color:#222;margin:-2px 0 5px}
.industry p{font-size:8.2px;line-height:9.8px;color:#555}
.blog-h{margin-top:6px}
.blog h4{font-weight:400;font-size:12.5px;color:var(--red);margin:-2px 0 5px}
.byline{font-size:8.5px;color:#333;margin-bottom:12px}
.byline em{color:var(--red);font-style:normal}
.blog ul{list-style:none}
.blog li{position:relative;padding-left:11px;font-size:8.2px;line-height:9.8px;color:#444;margin-bottom:9px}
.blog li::before{content:"";position:absolute;left:0;top:2px;width:5px;height:5px;border-radius:50%;background:var(--red)}
.blog a{display:block;margin-top:15px;font-size:9.5px;color:#222}
/* footer */
.foot-links{left:93px;top:1082px;width:694px;border-top:1px solid var(--line);border-bottom:1px solid var(--line);height:40px;display:flex;justify-content:space-between;align-items:center;font-size:8.5px;color:#333}
.pay{color:var(--red);display:flex;align-items:center;gap:8px}
.pay strong{font-size:13px;color:#1b3e7a;font-weight:700}
.copy{left:0;width:881px;text-align:center;font-size:8.2px;color:#444}
.copy em{color:var(--red);font-style:normal}
</style>
</head>
<body>
<header>
  <div class="abs brand-mark"></div>
  <div class="abs brand-name">Brixton Fabrication and Tooling, LLC</div>
  <div class="abs brand-tag">CNC Milling &amp; Turning, Production Machining, Ice Fishing Spears</div>
  <div class="abs phone"><svg width="16" height="20" viewBox="0 0 16 20"><path d="M4 1l3 4-2 2c1 3 3 6 5 7l2-2 3 3-2 3C6 18 1 10 2 3z" fill="#333"/></svg>555-010-0303</div>
  <div class="abs search">Search for Products<svg width="16" height="16" viewBox="0 0 16 16"><circle cx="6.5" cy="6.5" r="4.5" fill="none" stroke="#222" stroke-width="2"/><path d="M10 10l5 5" stroke="#222" stroke-width="2.5"/></svg></div>
  <div class="abs cart"><svg width="30" height="22" viewBox="0 0 30 22"><path d="M1 2h5l4 13h15l3-10H8" fill="none" stroke="#222" stroke-width="2.5"/><circle cx="12" cy="19" r="2" fill="#222"/><circle cx="23" cy="19" r="2" fill="#222"/></svg>My Cart (0)</div>
  <nav class="abs nav"><span>Home</span><span>Online Product Sales</span><span>Ice Fishing Spears</span><span>About us / Industries Served</span><span>Equipment</span><span>Contact Us</span><span>Our Blog</span></nav>
</header>

<section class="abs hero">
  <div class="abs hero-photo" role="img" aria-label="Rust-patina triple gear wall clock"></div>
  <div class="abs hero-panel">
    <h2>Triple Gear Clock</h2>
    <p>CNC Plasma cut gear clock with a rust patina. Clear coat finish. Material is 16ga steel. Approximate Dimensions are 21" x 13". Made in Michigan by Brixton Fabrication and Tooling, LLC</p>
    <div class="hero-price">Price: $150.00</div>
    <span class="buy">BUY NOW!</span>
    <div class="abs dots"><i></i><i class="on"></i><i></i></div>
  </div>
</section>

<h1 class="abs welcome" style="font-weight:400">WELCOME TO <b>BRIXTON FABRICATION &amp; TOOLING, LLC</b></h1>
<section class="abs intro">
  <div class="intro-photo"><div role="img" aria-label="Owners standing beside a CNC milling machine"></div></div>
  <h3>Your Manufacturing Experts.</h3>
  <p>We are your CNC milling and turning go-to facility. Our manufacturing facility is located in Marlow Point, Michigan and is equipped to perform a variety of machining services, including three axis CNC milling, "lights out" CNC turning, CNC Plasma Cutting, fully automatic sawing, prototype machining, long and short run production.</p>
  <p>Brixton Fabrication is proudly owned and operated by Owen and Marcus Hale. We have the capability, experience and know- how to solve even your most complex manufacturing problems. We stand behind the services we offer and guarantee your satisfaction.</p>
</section>
<div class="abs veteran">
  <div class="veteran-badge"></div>
  <div><h4>Thanks for stopping by.</h4><span>RNVR Veteran Owned Business</span></div>
</div>

<section class="abs featured">
  <div class="featured-head"><h3>Featured Products</h3><a>View all Products</a></div>
  <div class="grid">
    <div><div class="card-img"><div class="wings" role="img" aria-label="Gear clock with wings"></div></div><div class="card-info">Gear Clock with Wings<br>Price &nbsp;$155.00<div class="card-links"><span>View deatails</span><span>+ Add to Cart</span></div></div></div>
    <div><div class="card-img"><div class="gears" role="img" aria-label="Triple gear clock"></div></div><div class="card-info">Triple Gear Clock<br>Price: &nbsp;$150.00<div class="card-links"><span>View deatails</span><span>+ Add to Cart</span></div></div></div>
    <div><div class="card-img"><div class="sun" role="img" aria-label="Sun clock"></div></div><div class="card-info">Sun Clock<br>Price: &nbsp;$150.00<div class="card-links"><span>View deatails</span><span>+ Add to Cart</span></div></div></div>
    <div><div class="card-img"><div class="wings" role="img" aria-label="Gear clock with wings"></div></div><div class="card-info">Gear Clock with Wings<br>Price &nbsp;$155.00<div class="card-links"><span>View deatails</span><span>+ Add to Cart</span></div></div></div>
    <div><div class="card-img"><div class="gears" role="img" aria-label="Triple gear clock"></div></div><div class="card-info">Triple Gear Clock<br>Price: &nbsp;$150.00<div class="card-links"><span>View deatails</span><span>+ Add to Cart</span></div></div></div>
    <div><div class="card-img"><div class="sun" role="img" aria-label="Sun clock"></div></div><div class="card-info">Sun Clock<br>Price: &nbsp;$150.00<div class="card-links"><span>View deatails</span><span>+ Add to Cart</span></div></div></div>
  </div>
</section>

<aside class="abs side">
  <h2 class="side-h" style="font-weight:400">Industries We <b>Served</b></h2>
  <div class="industry"><div class="thumb"><div style="background:linear-gradient(135deg,#777,#222)" role="img" aria-label="Stack of machined pallet pins"></div></div><div><h5>Automation Equipment</h5><p>Pin pallet pins for repeatable blank positioning for conventional and robotic destackers</p></div></div>
  <div class="industry"><div class="thumb"><div style="background:linear-gradient(135deg,#aaa,#444)" role="img" aria-label="Rows of stainless pool hardware parts"></div></div><div><h5>Swimming Pool Hardware</h5><p>Commercial grade pool lift mounting hardware.<br>"304 Stainless Steel, 5/8-11 threaded blind hole, 2" deep."</p></div></div>
  <div class="industry"><div class="thumb"><div style="background:linear-gradient(#6b8fc0,#d9a45a)" role="img" aria-label="Roadside billboard"></div></div><div><h5>Commercial Advertising</h5><p>Commercial grade pool lift mounting hardware.<br>"304 Stainless Steel, 5/8-11 threaded blind hole, 2" deep."</p></div></div>
  <div class="industry"><div class="thumb"><div style="background:#fff;display:flex;align-items:center;justify-content:center;font-size:10px;color:var(--red)">Hullmark</div></div><div><h5>Marine</h5><p>Custom stern drive installation tools</p></div></div>
  <div class="industry"><div class="thumb"><div style="background:linear-gradient(#cfd8e0,#6c7680)" role="img" aria-label="Angler on the ice holding a fishing spear"></div></div><div><h5>Fishing</h5><p>Custom stern drive installation tools</p></div></div>
  <h2 class="side-h blog-h" style="font-weight:400">Our Recent <b style="font-weight:400">Blogs</b></h2>
  <div class="blog">
    <h4>2012 Year in Review</h4>
    <div class="byline"><em>Owen Hale:</em> Posted on Saturday, December 22, 2012</div>
    <ul>
      <li>Acquired new equipment. (Keystone Automatic band saw, and a Apex cold saw) Diversifying our sawing capabilities not only lets us quote more projects it also drives the cost lower to benefit our customers.</li>
      <li>Formed an LLC. We are now officially Brixton Fabrication and Tooling, LLC</li>
      <li>In October, 2012 we purchased a new building for our operations. We are still in the renovation phase but hope to be fully moved in and operational by the spring of 2013.</li>
      <li>We thank all of our customers and friends that helped make 2012 a great success!</li>
    </ul>
    <a>View all blog posts</a>
  </div>
</aside>

<footer>
  <div class="abs foot-links"><span>Home | Online Product Sales | Ice Fishing Spears | About Us / Industries Served | Equipment | Contact Us | Brixton Fabrication Blog</span><span class="pay">Secure payments by <strong>SafePay</strong><svg width="10" height="12" viewBox="0 0 10 12"><path d="M2 5V3a3 3 0 016 0v2" fill="none" stroke="#999" stroke-width="1.5"/><rect x="1" y="5" width="8" height="7" fill="#999"/></svg></span></div>
  <p class="abs copy" style="top:1141px">Copyright © 2014 <em>BRIXTON FABRICATION &amp; TOOLING, LLC.</em> Use of this website constitutes acceptance of our User Agreement and Privacy Policy.</p>
  <p class="abs copy" style="top:1161px">*Conditions apply please see our money back refund policy.</p>
</footer>
</body>
</html>
```